Pamphlet for introducing people to our church

I would like a church pamphlet designed, that includes the content in file "tovik-pamphlet.txt".

I am looking for a design that will incorporate the content in a professional and creative manner.

You do not have to use the content in any specific order, but I am relying on your skill and design knowledge to organize everything in an artistic and effective way.

Target Market(s)

Everyone

Industry/Entity Type

Religious

Requirements
Must have
• logo, use of content provided, use of branding (logo colors)
Nice to have
• More images where necessary
Should not have
• cross

```html
<!DOCTYPE html>
<html lang="en">
<head>
<meta charset="utf-8">
<title>Tovik – Church Pamphlet</title>
<link rel="stylesheet" href="https://fonts.googleapis.com/css2?family=Marcellus&family=Great+Vibes&family=Cormorant+SC:wght@500&family=Source+Sans+3:wght@300;400&display=swap">
<style>
  :root{
    --navy:#2b4461;
    --navy-deep:#1d3150;
    --orange:#f39533;
    --orange-soft:#f7a447;
    --ink:#222;
    --paper:#fff;
    --mist:#d9e2ea;
  }
  *{box-sizing:border-box;margin:0;padding:0}
  html,body{width:849px;height:1200px;overflow:hidden;background:var(--paper)}
  .sheet{position:relative;width:849px;height:1200px;border:1px solid #bbb;font-family:"Source Sans 3",sans-serif}
  .label{position:absolute;font:400 9px/1 Arial,sans-serif;color:var(--ink);transform:translateX(-50%)}
  .panel{position:absolute;overflow:hidden}

  /* Back panel */
  .back{left:102px;top:92px;width:322px;height:497px;background:var(--navy)}
  .back .brand{position:absolute;left:0;right:0;top:222px;text-align:center}
  .brand-name{font-family:"Marcellus",serif;color:#fff;font-size:46px;letter-spacing:1px;line-height:1}
  .back .rule{position:absolute;left:0;top:299px;width:100%;height:6px;background:var(--orange)}
  .contact{position:absolute;left:51px;list-style:none;color:#e6ebf1;font-size:8px;line-height:11px;font-weight:300}
  .contact li{position:absolute;left:0;width:260px;padding-left:20px}
  .contact strong{font-weight:400;color:#fff}
  .contact .dot{position:absolute;left:0;width:12px;height:12px;border-radius:50%;background:var(--orange)}
  .contact svg{position:absolute;left:3px;top:3px;width:6px;height:6px}

  /* Front panel */
  .front{left:424px;top:92px;width:322px;height:497px}
  .front .photo{position:absolute;inset:0;background:
      radial-gradient(ellipse 60% 45% at 55% 12%,#fff6cf 0%,#f7c04e 35%,rgba(210,120,30,.6) 60%,transparent 80%),
      linear-gradient(180deg,#b8741f 0%,#8b5a26 35%,#3f4f6a 60%,#1b3d78 80%,#0e2148 100%)}
  .front .badge{position:absolute;right:8px;top:8px;width:64px;height:64px;background:var(--navy);display:flex;align-items:center;justify-content:center}
  .front .badge span{font-family:"Marcellus",serif;color:#fff;font-size:15px}
  .front .title{position:absolute;left:0;right:0;top:328px;text-align:center;color:#fff;text-shadow:0 2px 4px rgba(0,0,0,.45);font-weight:400}
  .title .script{font-family:"Great Vibes",cursive;font-size:36px;line-height:30px;margin-left:-20px}
  .title .caps{font-family:"Marcellus",serif;font-size:54px;line-height:46px;letter-spacing:1px}

  /* Inside spread */
  .inside{left:102px;top:610px;width:644px;height:496px;background:var(--navy)}
  .inside .wedge{position:absolute;inset:0}
  .inside .scene{position:absolute;left:30px;top:28px;width:584px;height:360px;background:
      radial-gradient(circle at 85% 14%,#fff 0%,rgba(255,255,255,.8) 7%,rgba(255,255,255,.15) 18%,transparent 30%),
      linear-gradient(180deg,#2f4a68 0%,#5e7893 30%,#b3c2cf 48%,#c9ad80 62%,#7b5a3a 78%,#3a2c24 100%)}
  .mission{position:absolute;left:39px;top:32px;width:340px;color:var(--mist)}
  .mission h2{font-family:"Cormorant SC",serif;font-weight:500;font-size:19px;color:#fff;line-height:22px;margin-bottom:4px}
  .mission p{font-size:7.6px;line-height:10.8px;font-weight:300;margin-bottom:10px}
  .ministries{position:absolute;left:30px;top:388px;width:584px;height:86px;background:var(--orange)}
  .ministries h2{position:absolute;left:0;top:-21px;width:106px;height:21px;background:var(--navy);font-family:"Cormorant SC",serif;font-weight:500;font-size:17px;line-height:21px;color:var(--orange-soft);padding-left:9px}
  .ministries ul{position:absolute;left:67px;top:2px;width:511px;list-style:none;font-family:"Cormorant SC",serif;font-weight:500;font-size:13.5px;line-height:14px;letter-spacing:.4px;color:#fff}
  .ministries li{position:relative;margin-bottom:1px}
  .ministries li::before{content:"\2737";position:absolute;left:-12px;top:0;color:var(--navy);font-size:9px}
</style>
</head>
<body>
<div class="sheet">
  <span class="label" style="left:263px;top:81px">Back</span>
  <span class="label" style="left:585px;top:81px">Front</span>
  <span class="label" style="left:424px;top:599px">Inside</span>

  <section class="panel back">
    <div class="brand">
      <div class="brand-name">TOVIK</div>
    </div>
    <div class="rule"></div>
    <ul class="contact">
      <li style="top:334px"><span class="dot"><svg viewBox="0 0 6 6"><circle cx="3" cy="3" r="2.4" fill="none" stroke="#fff" stroke-width=".8"/><path d="M3 1.6V3h1" stroke="#fff" stroke-width=".7" fill="none"/></svg></span><strong>Sunday Service:</strong><br>10:00am-12:30pm</li>
      <li style="top:365px"><span class="dot"><svg viewBox="0 0 6 6"><path d="M3 6C1.5 4 1 3.2 1 2.2a2 2 0 0 1 4 0C5 3.2 4.5 4 3 6z" fill="#fff"/></svg></span><strong>Alder Hill Community Hall</strong><br>48 Linden Row, Fairhaven, ME 04190<br>Visit us at www.tovik.org</li>
      <li style="top:407px"><span class="dot" style="top:11px"><svg viewBox="0 0 6 6"><path d="M1.2 .8l1.2 1.3-.6.8c.4.8.9 1.3 1.7 1.7l.8-.6 1.3 1.2-.8.8C2.6 5.6.4 3.4.4 1.6z" fill="#fff"/></svg></span>If you need prayer or counseling<br>give us a call at <strong>+1 555-014-2280</strong></li>
      <li style="top:439px"><span class="dot"><svg viewBox="0 0 6 6"><rect x=".5" y="1.3" width="5" height="3.4" fill="none" stroke="#fff" stroke-width=".7"/><path d="M.5 1.3L3 3.3l2.5-2" fill="none" stroke="#fff" stroke-width=".7"/></svg></span>or email us at <strong>hello@cedarmeadow.org</strong></li>
    </ul>
  </section>

  <section class="panel front">
    <div class="photo" role="img" aria-label="Praying hands over an open Bible in rays of golden light above a blue city skyline"></div>
    <div class="badge"><span>TOVIK</span></div>
    <h1 class="title">
      <div class="script">A Voice</div>
      <div class="caps">TO THE</div>
      <div class="caps">NATIONS</div>
    </h1>
  </section>

  <section class="panel inside">
    <svg class="wedge" viewBox="0 0 644 496" preserveAspectRatio="none">
      <polygon points="0,0 399,0 370,496 0,496" fill="var(--orange)"/>
    </svg>
    <div class="scene" role="img" aria-label="Spotlight shining over a full church congregation gathered in worship"></div>
    <div class="mission">
      <h2>Mission Statement:</h2>
      <p>TOVIK is a gathering of believers whose purpose is to seek the face of God for an authentic restoration of the church as a body of born again believers around the world. As a gathering of believers, TOVIK seeks an awakening of the mind founded on the precepts and teachings of Jesus Christ. The modern church has replaced the simple and Kingdom centered principles of Jesus's disciples with complacent and compromised teachings on earthly prosperity.</p>
      <p>We believe in humbly seeking God without motive to use God or His Word for our own gain. The end times church will experience a glorious revival, renewed love and zeal for true discipleship, faith, and godliness as Jesus intended for us.</p>
    </div>
    <div class="ministries">
      <h2>Ministries:</h2>
      <ul>
        <li>Kingdom seeds (Children's ministry)Children learn to be seeds of godliness in the world.</li>
        <li>School of pilgrims Learn the basics of Christian faith and about God's purpose for your life.</li>
        <li>School of disciplesDeepen your knowledge of God's word and learn how to server him.</li>
      </ul>
    </div>
  </section>
</div>
</body>
</html>
```